Stationary pack for BrightVane

BrightVane is a recently establish Solar brokerage company based in Australia. We have a number of sales staff who provide advice and guidance to both residential and commercial customers regarding solar systems (solar hot water and solar panels.)

In addition to our brokerage services we are also developing software for the solar industry, which will be used to automate the solar system install process. This system will be used by other companies in the solar industry including installers, wholesalers and government departments.

We are after a stationary pack that consists of the following: Business cards, compliments slip and letter head.

The EPS, AI, PNG etc files for the logo are attached.

For the business card:
The name and logo of the company need to be clearly visible. On the back of the business cards, we would like the logo. I am happy for you to split the image part of the logo from the text if you think it would look better a different way.

I would like the business cards to be easily readable with the following information on the front:
Name
(Please leave room for titles for the future – eg Sales Advisor.)
Mobile
Office
Email
Address
ABN

Letter heads:
I would prefer the address to be at the top

Compliments slips:
Only need to be one sided

Target Market(s)

BrightVane provides services to both residential and commercial customers. Our customers will be environmentally conscious.

Industry/Entity Type

Residential

Requirements
Must have
• Business cards must have the logo on the back.

```html
<!DOCTYPE html>
<html lang="en">
<head>
<meta charset="utf-8">
<title>BrightVane Stationery Pack</title>
<link rel="stylesheet" href="https://fonts.googleapis.com/css2?family=Poppins:wght@600&family=Arimo:wght@400;700&display=swap">
<style>
  :root {
    --stage: #000000;
    --paper: #ffffff;
    --green: #5a9e2a;
    --green-soft: #8cc63f;
    --blue: #1f5a9e;
    --orange: #f39a00;
    --yellow: #ffd21a;
    --pale-yellow: #fff2a8;
    --ink: #555555;
    --muted: #8a8a8a;
  }
  * { margin: 0; padding: 0; box-sizing: border-box; }
  html, body { width: 1200px; height: 900px; overflow: hidden; background: var(--stage); }
  body { position: relative; font-family: "Arimo", Arial, sans-serif; color: var(--ink); }

  .sheet { position: absolute; background: var(--paper); overflow: hidden; }

  .brand { display: flex; align-items: center; gap: 8px; font-family: "Poppins", sans-serif; font-weight: 600; color: var(--green); line-height: 1; white-space: nowrap; }
  .brand-dot { border-radius: 50%; background: var(--green); flex: none; }

  .band { position: absolute; left: 0; right: 0; background: linear-gradient(90deg, var(--orange), var(--yellow) 70%, var(--pale-yellow)); }

  /* Letterhead */
  .letterhead { left: 64px; top: 80px; width: 528px; height: 740px; }
  .letterhead .brand { position: absolute; top: 64px; left: 50%; transform: translateX(-50%); flex-direction: column; gap: 8px; font-size: 26px; }
  .letterhead .brand .brand-dot { width: 36px; height: 36px; }
  .letterhead .header-address { position: absolute; left: 0; right: 0; top: 144px; text-align: center; font-size: 11px; line-height: 16px; letter-spacing: 1px; color: var(--muted); }
  .letterhead .band { top: 686px; height: 44px; }
  .letterhead .footer-dot { position: absolute; right: 22px; top: 694px; width: 36px; height: 36px; border-radius: 50%; background: var(--green); border: 3px solid var(--paper); }

  /* Business card front */
  .card-front { left: 666px; top: 122px; width: 220px; height: 124px; border-radius: 8px; background: linear-gradient(180deg, var(--paper) 78%, var(--pale-yellow) 86%, var(--yellow)); }
  .card-front .person { position: absolute; left: 16px; top: 16px; }
  .card-front .name { font-size: 9px; font-weight: 700; color: var(--blue); }
  .card-front .title { font-size: 6px; margin-top: 2px; }
  .card-front .details { position: absolute; left: 16px; top: 44px; font-size: 6px; line-height: 9px; }
  .card-front .brand { position: absolute; right: 18px; top: 36px; flex-direction: column; gap: 4px; font-size: 14px; }
  .card-front .brand .brand-dot { width: 22px; height: 22px; }

  /* Business card back */
  .card-back { left: 902px; top: 122px; width: 222px; height: 124px; border-radius: 8px; background: radial-gradient(circle at 80% 40%, var(--yellow), var(--orange) 90%); }
  .card-back .tagline { position: absolute; left: 14px; top: 66px; font-size: 6px; color: var(--paper); }
  .card-back .mark-area { position: absolute; right: 14px; top: 16px; width: 92px; height: 92px; border-radius: 50%; background: radial-gradient(circle, var(--yellow) 30%, var(--green-soft) 70%, var(--green)); }

  /* Compliment slip */
  .comp-slip { left: 634px; top: 292px; width: 526px; height: 244px; }
  .comp-slip .brand { position: absolute; left: 18px; top: 12px; flex-direction: column; gap: 6px; font-size: 18px; }
  .comp-slip .brand .brand-dot { width: 28px; height: 28px; }
  .comp-slip .address { position: absolute; left: 132px; top: 28px; font-size: 9px; line-height: 11px; color: var(--muted); }
  .comp-slip .heading { position: absolute; left: 20px; top: 92px; font-size: 19px; font-weight: 700; color: var(--blue); }
  .comp-slip .band { top: 220px; height: 24px; }
  .comp-slip .web { position: absolute; right: 62px; top: 224px; font-size: 10px; color: var(--ink); }
  .comp-slip .footer-dot { position: absolute; right: 16px; top: 196px; width: 40px; height: 40px; border-radius: 50%; background: var(--green); border: 3px solid var(--paper); }

  /* Large promo card */
  .promo-card { left: 634px; top: 562px; width: 526px; height: 246px; background: radial-gradient(circle at 80% 45%, var(--yellow), var(--orange) 85%); }
  .promo-card .brand { position: absolute; left: 50px; top: 102px; font-size: 34px; color: var(--paper); }
  .promo-card .web { position: absolute; left: 52px; top: 144px; font-size: 11px; color: var(--paper); }
  .promo-card .mark-area { position: absolute; right: 20px; top: 20px; width: 206px; height: 206px; border-radius: 50%; background: radial-gradient(circle, var(--yellow) 30%, var(--green-soft) 68%, var(--green)); }
</style>
</head>
<body>

<section class="sheet letterhead" aria-label="Letterhead">
  <div class="brand"><span class="brand-dot"></span>BrightVane</div>
  <p class="header-address">48 Harbour Lane Sydney, NSW 2000<br>Phone 1-800-555-0147 Email: info@brightvane.com.au</p>
  <div class="band"></div>
  <span class="footer-dot"></span>
</section>

<section class="sheet card-front" aria-label="Business card front">
  <div class="person">
    <p class="name">Alex Reed</p>
    <p class="title">Sales Advisor</p>
  </div>
  <p class="details">12 Harbour Ln<br>Sydney NSW 2000<br>M 0400 555 012<br>O 02 5550 1234<br>E alex@brightvane.com.au<br>ABN 12 345 678 901</p>
  <div class="brand"><span class="brand-dot"></span>BrightVane</div>
</section>

<section class="sheet card-back" aria-label="Business card back">
  <p class="tagline">www.brightvane.com.au</p>
  <div class="mark-area" role="img" aria-label="Large green and yellow brand emblem"></div>
</section>

<section class="sheet comp-slip" aria-label="Compliments slip">
  <div class="brand"><span class="brand-dot"></span>BrightVane</div>
  <p class="address">BrightVane Pty Ltd<br>12 Harbour Lane 2000 AA<br>NSW Australia</p>
  <h1 class="heading">With Compliment</h1>
  <div class="band"></div>
  <p class="web">www.brightvane.com.au</p>
  <span class="footer-dot"></span>
</section>

<section class="sheet promo-card" aria-label="Brand card">
  <div class="brand">BrightVane</div>
  <p class="web">www.brightvane.com.au</p>
  <div class="mark-area" role="img" aria-label="Large green and yellow brand emblem"></div>
</section>

</body>
</html>
```